7 Herons Distillery - Bottle Label Design

We are a small craft distillery whose branding needs to incorporate our location on a lake (Lac Vernisse, Quebec, Canada). A unique aspect of the lake is that people drive floating docks on the lake powered by a small outboard motor (see photos). Back in the 1970’s when Lac Vernisse was a sparsely populated and difficult-to-access lake in the Gatineau Hills north of Ottawa, the concept of motorized docks was conjured on a lazy afternoon and this single stroke of genius has inadvertently spawned the most exceptional and eccentric lake based community. Throughout the summer, somewhere around four o’clock on any given Friday and Saturday it starts to happen. Docks set sail from their customary landing places - family, friends, snacks and loaded drink coolers in-tow and, as if magnetically drawn, head toward Pine Shoal. Without fail they will come upon a gathering of similar minded floating docks within the vicinity - be guided in with help to moor alongside and within seconds be seamlessly immersed in the festivities. Seldom any longer are these events planned, they have become elemental, a thing organically derived from within the community. This on-going weekly event is the genesis of the strong bond that brings us Seven Herons Distilling.
Each of the 4 distillery owners have one of these docks so hence the name. We are open to either "7 Herons" or spelled out as "Seven Herons" as may be visually appropriate. We are also open to "Distillery" or "Distilling". More detail on the docks themselves, they are 14x16 feet powered by a small outboard motor as shown in the photos. This dock aspect may be difficult to incorporate into the branding but the lake outline is included as an image applicable to include for that local reference aspect. We will be creating very high quality small batch liquors such as vodka, rum, gin and whiskey. Each batch will be triple distilled and perhaps 20 bottles in quantity so very exclusive. We are aiming at a premium feel for the branding. Attached are some bottle label designs that evoke the type of feel we are going for and a photo of the style of blank bottle to design for which is a 750ml Nordic pattern bottle.
In general we are going for more contemporary than traditional, more bold than delicate. If a single label the size desired would be 4 inches wide and 4 inches tall. If a double/split label as in two of the photos the top label would be 3 inches wide and 3 inches tall and the bottom label would be max 4 inches wide and 1.5 inches tall. We are open to the upper label being a "transparent" label to create a printed on bottle effect, perhaps of the brand logo. We are only interested in front label so do not require a back, neck or closure label. The label will require the ability to name the batch style name (example "Tuberix") and then the amplifying information for the type of alcohol (Russian Potato Vodka) in a smaller font. Another example ("Red Fox" and "London Dry Gin"). Information for bottle size (750ml) and alcohol % (40%) are also to be included. Governmental safety warnings are not required. We are open to use of any colours in the label. The basic label design would be re-used for different types of batches where we would change the style and alcohol name.
Updates

Target Market(s)

Up scale premium spirits buyers

Font styles to use
Serif
Sans Serif

Requirements
Must have
• A visual reference to the docks or the lake per the images attached.
Nice to have
• Ideally we can re-use the label design for a different type of Alcohol by changing the alcohol name and style information and maybe the colour of a major element in the label.

```html
<!DOCTYPE html>
<html lang="en">
<head>
<meta charset="utf-8">
<title>Seven Herons Distilling – Red Fox London Dry Gin Label</title>
<link rel="stylesheet" href="https://fonts.googleapis.com/css2?family=Montserrat:wght@800&family=Outfit:wght@700&family=Barlow:wght@700&display=swap">
<style>
  :root {
    --label-yellow: #fcd23e;
    --lake-cream: #f6ebb8;
    --ink: #111111;
    --paper: #ffffff;
  }
  html, body {
    margin: 0;
    padding: 0;
    width: 1200px;
    height: 1200px;
    overflow: hidden;
    background: var(--paper);
  }
  .label {
    position: relative;
    width: 1200px;
    height: 1200px;
  }
  .brand-disc {
    position: absolute;
    left: 556px;
    top: 85px;
    width: 480px;
    height: 480px;
    border-radius: 50%;
    background: var(--label-yellow);
  }
  .brand-name {
    position: absolute;
    left: 121px;
    top: 150px;
    width: 430px;
    margin: 0;
    font-family: "Montserrat", sans-serif;
    font-weight: 800;
    color: var(--ink);
    line-height: 0.95;
    letter-spacing: -1px;
  }
  .brand-name .brand-word {
    display: block;
    font-size: 88px;
  }
  .brand-name .brand-trade {
    display: block;
    font-size: 44px;
    margin-top: 22px;
    letter-spacing: 3px;
  }
  .style-name {
    position: absolute;
    left: 0;
    top: 712px;
    width: 1200px;
    margin: 0;
    text-align: center;
    font-family: "Outfit", sans-serif;
    font-weight: 700;
    font-size: 150px;
    line-height: 1;
    color: var(--label-yellow);
    -webkit-text-stroke: 5px var(--ink);
    paint-order: stroke fill;
  }
  .spirit-band {
    position: absolute;
    left: 127px;
    top: 862px;
    width: 951px;
    height: 282px;
    background: var(--label-yellow);
  }
  .spirit-type {
    position: absolute;
    left: 0;
    top: 20px;
    width: 100%;
    margin: 0;
    text-align: center;
    font-family: "Barlow", sans-serif;
    font-weight: 700;
    font-size: 66px;
    line-height: 1;
    color: var(--ink);
  }
  .lake-outline {
    position: absolute;
    left: 385px;
    top: 90px;
    width: 320px;
    height: 120px;
    border-radius: 50% 40% 55% 45%;
    background: var(--lake-cream);
  }
  .bottle-facts {
    position: absolute;
    left: 0;
    bottom: 12px;
    width: 100%;
    margin: 0;
    text-align: center;
    font-family: "Barlow", sans-serif;
    font-weight: 700;
    font-size: 26px;
    color: var(--ink);
  }
</style>
</head>
<body>
  <main class="label">
    <div class="brand-disc"></div>
    <h1 class="brand-name">
      <span class="brand-word">SEVEN</span>
      <span class="brand-word">HERONS</span>
      <span class="brand-trade">DISTILLING</span>
    </h1>

    <h2 class="style-name">RED FOX</h2>

    <section class="spirit-band">
      <p class="spirit-type">LONDON DRY GIN</p>
      <div class="lake-outline" role="img" aria-label="Outline map of Lac Vernisse"></div>
      <p class="bottle-facts">45% ALC/VOL | 80 PROOF | 750 ML</p>
    </section>
  </main>
</body>
</html>
```